Swing Dance Themed Cleaning Company Website

We need a website designed for a cleaning company based in Portland, Oregon called Bellhop Sweep. We clean homes and commercial buildings, inside and out.

needs to be vintage and like the velvet marlow. Speakeasy 1920s feel.
needs to be classy.

Check out bellhopsweep.com We are not happy with the site currently.

please look at house finderly site for more content https://www.housefinderly.com/rated.BellhopSweepCleaning.48217065.html

Check out my videos on my ClipHarbor channel Bellhop Sweep

Target Market(s)

middle class and home owner

Industry/Entity Type

Cleaning Service

Number of Pages Required

3 page

Font styles to use
Other font styles liked:
• jazzrag

Colors

Designer to choose colors to be used in the design.

Requirements
Must have
• must be good on pc and mobile

```html
<!DOCTYPE html>
<html lang="en">
<head>
<meta charset="utf-8">
<title>Bellhop Sweep – Keep Cleaning Classy Portland</title>
<link rel="stylesheet" href="https://fonts.googleapis.com/css2?family=Poiret+One&family=Lato:ital,wght@0,400;0,700;1,400&display=swap">
<style>
:root{
  --gold:#e6a90b;
  --ink:#111111;
  --text:#4d4d4d;
  --muted:#6a6a6a;
  --paper:#ffffff;
  --footer:#333333;
  --card-line:#d9d9d9;
}
*{box-sizing:border-box;margin:0;padding:0}
html,body{width:1200px;height:3564px;overflow:hidden}
body{position:relative;background:var(--paper);font-family:"Lato",Arial,sans-serif;color:var(--text)}
.deco{font-family:"Poiret One","Lato",sans-serif;font-weight:400;color:var(--gold);text-transform:uppercase;-webkit-text-stroke:.9px currentColor}

/* header */
.site-header{position:absolute;left:0;top:0;width:1200px;height:124px;background:linear-gradient(90deg,#e9e6e1,#f4f2ee 40%,#e6e3de);border-top:7px solid var(--gold)}
.brand{position:absolute;left:0;top:0;width:1200px;height:117px;display:flex;align-items:center;justify-content:center;gap:12px}
.brand-mark{width:16px;height:16px;background:var(--ink)}
.brand-name{font-family:"Lato",sans-serif;font-weight:700;color:var(--ink);font-size:28px;letter-spacing:2px}
.main-nav{position:absolute;left:0;top:124px;width:1200px;height:54px;background:var(--gold)}
.nav-links{position:absolute;left:78px;top:0;height:54px;display:flex}
.nav-links a{display:block;height:54px;line-height:54px;padding:0 22px;font-size:15px;color:var(--ink);text-decoration:none;text-transform:uppercase}
.nav-links a.active{background:var(--ink);color:#fff}
.call-now{position:absolute;left:943px;top:0;width:178px;height:54px;background:var(--ink);color:var(--gold);font-family:"Poiret One",sans-serif;font-size:20px;line-height:54px;text-align:center;text-decoration:none;-webkit-text-stroke:.6px currentColor}

/* hero */
.hero{position:absolute;left:0;top:178px;width:1200px;height:563px;background:linear-gradient(90deg,#8b6b50 0%,#c6a98b 30%,#e6d8c6 55%,#b8ad9a 100%)}
.hero-photo{position:absolute;left:820px;top:20px;width:340px;height:543px;background:linear-gradient(180deg,#dab9a0 0%,#7fb79a 45%,#5e9e82 100%);opacity:.85}
.hero-title{position:absolute;left:78px;top:185px;font-size:62px;line-height:84px;-webkit-text-stroke:1.6px currentColor;text-shadow:0 2px 6px rgba(0,0,0,.35)}

/* about */
.about-art{position:absolute;left:0;top:780px;width:570px;height:430px;background:radial-gradient(ellipse at 40% 50%,#eadfd6 0%,#f7f3ef 60%,#ffffff 100%)}
.about-copy{position:absolute;left:634px;top:820px;width:490px}
.section-title{font-size:42px;line-height:54px}
.about-lead{font-style:italic;font-size:17px;color:var(--muted);margin-top:10px}
.about-sub{font-size:28px;margin-top:14px;line-height:34px}
.about-text{font-size:15px;line-height:26px;margin-top:6px;color:var(--text)}
.btn-ribbon{display:inline-block;background:var(--ink);color:var(--gold);font-family:"Poiret One",sans-serif;font-size:20px;text-transform:uppercase;text-decoration:none;text-align:center;-webkit-text-stroke:.6px currentColor}
.about-copy .btn-ribbon{width:176px;height:46px;line-height:46px;margin-top:22px}

/* services */
.services{position:absolute;left:0;top:1240px;width:1200px;height:530px;background:linear-gradient(90deg,#2b2a28,#4a4641 45%,#3a3733 70%,#262523)}
.services .section-title{position:absolute;left:0;top:44px;width:1200px;text-align:center}
.services-intro{position:absolute;left:260px;top:114px;width:680px;text-align:center;color:#fff;font-size:15px;line-height:27px}
.service{position:absolute;top:214px;width:250px;text-align:center;color:#fff}
.service-icon{width:114px;height:114px;margin:0 auto;border:2px solid var(--gold);border-radius:50%;display:flex;align-items:center;justify-content:center}
.service h3{font-size:22px;font-weight:700;margin-top:30px}
.service p{font-size:14px;line-height:24px;margin-top:6px}

/* blog */
.blog-title{position:absolute;left:0;top:1815px;width:1200px;text-align:center}
.post{position:absolute;top:1886px;width:333px;height:343px;border:2px solid var(--card-line);background:#fff}
.post-media{position:absolute;left:19px;top:19px;width:291px;height:185px;background:linear-gradient(135deg,#b7c6b3,#e8d6a8 55%,#c9b09a)}
.post-meta{position:absolute;left:0;bottom:0;width:100%;height:38px;background:rgba(230,169,11,.92);color:#fff;font-size:15px;line-height:38px;padding-left:22px}
.post h3{position:absolute;left:19px;top:224px;font-size:20px;font-weight:700;color:#333}
.post-rule{position:absolute;left:19px;top:263px;width:60px;height:2px;background:#555}
.post p{position:absolute;left:19px;top:280px;width:295px;font-size:15px;line-height:25px;color:#444}

/* contact */
.contact{position:absolute;left:0;top:2316px;width:1200px;height:583px;background:linear-gradient(90deg,#b39070 0%,#e6d9cb 40%,#cdb79e 70%,#8d6f55 100%)}
.contact-photo{position:absolute;left:120px;top:20px;width:340px;height:563px;background:linear-gradient(180deg,#dcbca4 0%,#86bb9f 40%,#5f9c80 100%);opacity:.85}
.contact-card{position:absolute;left:551px;top:108px;width:537px;height:399px;background:radial-gradient(ellipse at 50% 45%,#eed6a6 0%,#d9b376 60%,#a9793f 100%);box-shadow:0 6px 18px rgba(0,0,0,.35)}
.contact-card .section-title{position:absolute;left:0;top:70px;width:100%;text-align:center;color:var(--ink)}
.field{position:absolute;width:187px;height:43px;border:1px solid #7a5a2e;color:#3a2a12;font-size:14px;line-height:41px;padding-left:14px}
.contact-card .btn-ribbon{position:absolute;left:183px;top:261px;width:171px;height:47px;line-height:47px;clip-path:polygon(0 0,100% 0,92% 50%,100% 100%,0 100%,8% 50%)}

/* reach out */
.reach{position:absolute;left:78px;top:2958px;width:440px}
.reach p{font-size:15px;line-height:27px;margin-top:10px}
.contact-line{display:flex;align-items:flex-start;gap:14px;font-size:15px;line-height:25px;color:#555}
.reach-art{position:absolute;left:640px;top:2950px;width:480px;height:448px;background:radial-gradient(ellipse at 50% 50%,#e9ded3 0%,#f6f2ee 60%,#ffffff 100%)}

/* footer */
.site-footer{position:absolute;left:0;top:3398px;width:1200px;height:166px;background:var(--footer)}
.social{position:absolute;left:442px;top:38px;display:flex;gap:14px}
.social span{display:block;width:52px;height:46px;border:2px solid var(--gold)}
.copyright{position:absolute;left:0;top:106px;width:1200px;text-align:center;color:#fff;font-size:15px}
</style>
</head>
<body>

<header class="site-header">
  <div class="brand"><span class="brand-mark"></span><span class="brand-name">BELLHOP SWEEP</span></div>
</header>
<nav class="main-nav">
  <div class="nav-links">
    <a class="active" href="#">Home</a><a href="#">About</a><a href="#">Services</a><a href="#">Blog</a><a href="#">Contact</a>
  </div>
  <a class="call-now" href="#">CALL US NOW</a>
</nav>

<section class="hero" role="img" aria-label="Bright living room with a smiling retro-styled cleaner in a green striped dress holding a cloth and spray bottle">
  <div class="hero-photo"></div>
  <h1 class="hero-title deco">Keep Cleaning<br>Classy Portland</h1>
</section>

<div class="about-art" role="img" aria-label="Sepia line illustration of a vintage housekeeper wiping a window"></div>
<section class="about-copy">
  <h2 class="section-title deco">About Us</h2>
  <p class="about-lead">Making the greater Portland area clean, one building at a time</p>
  <h3 class="about-sub deco">Good People, Great Service</h3>
  <p class="about-text">Bellhop Sweep is a family owned professional cleaning business. We provide our years of cleaning experience to homes and businesses in and around Portland, Oregon. If you need something cleaned, have it cleaned the right way – contact us. Any doubts you have will be wiped away by our fantastic service and personable employees.</p>
  <a class="btn-ribbon" href="#">Know More</a>
</section>

<section class="services" role="img" aria-label="Dimmed photo of cleaners mopping and vacuuming a room">
  <h2 class="section-title deco">Our Services</h2>
  <p class="services-intro">We provide cleaning and janitorial services for one-time and recurring needs. While this isn't an exhaustive list of available services, these are certainly the most commonly requested!</p>

  <div class="service" style="left:72px">
    <div class="service-icon"><svg width="54" height="54" viewBox="0 0 54 54" fill="none" stroke="#fff" stroke-width="2"><path d="M16 6v26M10 32h12l3 16H7z"/><path d="M36 6v20M30 26h12v6H30zM32 32l-2 16h12l-2-16"/></svg></div>
    <h3>Janitorial Services</h3>
    <p>Routine janitorial, Tall cleaning, Food service sanitation, Clean room services</p>
  </div>
  <div class="service" style="left:341px">
    <div class="service-icon"><svg width="54" height="54" viewBox="0 0 54 54" fill="none" stroke="#fff" stroke-width="2"><path d="M6 26L27 8l21 18M12 22v24h30V22"/><rect x="22" y="32" width="10" height="14"/></svg></div>
    <h3>House-cleaning</h3>
    <p>Floors, Carpet cleaning, Refuse removal, Dusting, Interior windows, Blinds</p>
  </div>
  <div class="service" style="left:609px">
    <div class="service-icon"><svg width="54" height="54" viewBox="0 0 54 54" fill="none" stroke="#fff" stroke-width="2"><path d="M10 44l22-22M38 8a8 8 0 1 0 8 8l-6 2-4-4z"/><path d="M10 10l34 34M8 8l6 2-4 4z"/></svg></div>
    <h3>Maintenance</h3>
    <p>Pressure washing, Gutters, Painting, Exterior windows, Construction cleanup, Detailing</p>
  </div>
  <div class="service" style="left:878px">
    <div class="service-icon"><svg width="54" height="54" viewBox="0 0 54 54" fill="none" stroke="#fff" stroke-width="2"><rect x="8" y="11" width="38" height="34" rx="3"/><path d="M8 20h38M17 6v9M37 6v9M20 32l5 5 10-10"/></svg></div>
    <h3>Event services</h3>
    <p>Event hosting at our riverside studio Event cleanup</p>
  </div>
</section>

<h2 class="blog-title section-title deco">Blog Post</h2>
<article class="post" style="left:78px">
  <div class="post-media" role="img" aria-label="Cleaners in aprons wiping a table"><div class="post-meta">20 March, 2018 / 17 Views</div></div>
  <h3>The blog title</h3><div class="post-rule"></div>
  <p>Lorem Ipsum is simply dummy text of the printing and typesetting industry.</p>
</article>
<article class="post" style="left:435px">
  <div class="post-media" role="img" aria-label="Gloved hands cleaning a countertop"><div class="post-meta">20 March, 2018 / 17 Views</div></div>
  <h3>The blog title</h3><div class="post-rule"></div>
  <p>Lorem Ipsum is simply dummy text of the printing and typesetting industry.</p>
</article>
<article class="post" style="left:789px">
  <div class="post-media" role="img" aria-label="Cleaner holding a basket of cleaning supplies"><div class="post-meta">20 March, 2018 / 17 Views</div></div>
  <h3>The blog title</h3><div class="post-rule"></div>
  <p>Lorem Ipsum is simply dummy text of the printing and typesetting industry.</p>
</article>

<section class="contact">
  <div class="contact-photo" role="img" aria-label="Smiling retro-styled cleaner with gloves and spray bottle in a bright room"></div>
  <form class="contact-card" aria-label="Contact form on an aged parchment backdrop">
    <h2 class="section-title deco">Contact Us</h2>
    <div class="field" style="left:67px;top:138px">Name</div>
    <div class="field" style="left:276px;top:138px">Email</div>
    <div class="field" style="left:67px;top:202px">Phone</div>
    <div class="field" style="left:276px;top:202px">subject</div>
    <a class="btn-ribbon" href="#">Send Now</a>
  </form>
</section>

<section class="reach">
  <h2 class="section-title deco">Reach Out</h2>
  <p>We have a flexible team ready to meet your cleaning needs, servicing Multnomah, Washington, and Clackamas Counties. Offering cleaning, janitorial, and maintenance services for your home, apartment or business, we provide both one-time as well as weekly, bi-weekly or monthly cleaning services.</p>
  <p>If you're ready to experience a professional cleaning, reach out to us now!</p>
  <div class="contact-line" style="margin-top:20px">
    <svg width="20" height="26" viewBox="0 0 20 26"><path d="M10 1a8 8 0 0 0-8 8c0 6 8 16 8 16s8-10 8-16a8 8 0 0 0-8-8z" fill="var(--gold)"/><circle cx="10" cy="9" r="3" fill="#fff"/></svg>
    <div>Address<br>418 SE Alder Ct #12, Portland, OR 97214</div>
  </div>
  <div class="contact-line" style="margin-top:16px;align-items:center">
    <svg width="20" height="20" viewBox="0 0 20 20"><path d="M4 1l4 4-2 3c1 3 3 5 6 6l3-2 4 4-3 3C8 19 1 12 1 4z" fill="var(--gold)"/></svg>
    <span>971-555-0148</span>
    <svg style="margin-left:26px" width="22" height="16" viewBox="0 0 22 16" fill="none" stroke="var(--gold)" stroke-width="2"><rect x="1" y="1" width="20" height="14"/><path d="M1 1l10 8 10-8"/></svg>
    <span>office@bellhopsweep.com</span>
  </div>
</section>
<div class="reach-art" role="img" aria-label="Sepia line illustration of a vintage bellhop sweeping with a broom"></div>

<footer class="site-footer">
  <div class="social"><span></span><span></span><span></span><span></span><span></span></div>
  <p class="copyright">©BELLHOP SWEEP- 2018. All Rights Reserved.</p>
</footer>

</body>
</html>
```